Steady Harbor Leadership Roundtable Series Promotion

I'm wanting a single page (for now) website to promote my leadership training. Content would include: basic messaging what Steady Harbor means, invitation to join the Steady Harbor Roundtable workshops, have me come speak to them, join me on a leadership getaway, get personal coaching, watch some video links of Rud, then referrals of people saying nice things about Rud, connect to Rud’s personal website to learn more about me. The goal of the page is to 1) get people excited to attend a workshop, hear me speak, coach them, or join me on a getaway trip, 2) educate them in how they can get in control of their own life, and 3) link to my personal site to learn more about me. This is the general idea: https://www.perlwickstand.com/

Target Market(s)

Business owners or self improvement enthusiasts looking to take their businesses and personal lives to the next level.

Industry/Entity Type

Business Consultant

Coding

Coded - Design and coding required

Number of Pages Required

1 page

Font styles to use
Other font styles liked:
• See uploaded logo

Colors
0392cd

Requirements
Must have
• Fonts and colors that match the logo that was uploaded. Uplifting, inspirational look and feel.
Nice to have
• Similar to: https://www.perlwickstand.com/ and https://dorvankessling.com/

```html
<!DOCTYPE html>
<html lang="en">
<head>
<meta charset="utf-8">
<title>Steady Harbor Roundtable</title>
<link href="https://fonts.googleapis.com/css2?family=Cinzel:wght@400;700&family=Questrial&display=swap" rel="stylesheet">
<style>
:root{
  --blue:#0392cd;
  --blue-deep:#0a7fd0;
  --ink:#111111;
  --night:#0d0f14;
  --text:#2a2a2a;
  --muted:#8a8a8a;
  --white:#ffffff;
  --line:#d6d6d6;
}
*{margin:0;padding:0;box-sizing:border-box}
html,body{width:1200px;height:4125px;overflow:hidden;background:var(--white)}
body{position:relative;font-family:'Questrial',sans-serif;color:var(--text)}
.abs{position:absolute}
section,header,footer{position:absolute;left:0;width:1200px;overflow:hidden}
.serif{font-family:'Cinzel',serif}
.btn{position:absolute;display:flex;align-items:center;justify-content:center;border-radius:30px;font-size:18px}
.btn-solid{background:var(--blue-deep);color:var(--white)}
.btn-outline{border:2px solid var(--blue-deep);color:var(--blue-deep);background:transparent}
.btn-outline.on-dark{color:var(--white)}

/* header */
.site-header{top:0;height:95px;background:var(--ink)}
.brand{position:absolute;font-family:'Cinzel',serif;font-weight:700;color:var(--white);line-height:1.05}
.site-header .brand{left:90px;top:22px;font-size:22px;width:200px}
.main-nav{position:absolute;left:375px;top:35px;display:flex;gap:31px;font-size:15px;color:var(--white)}

/* hero */
.hero{top:95px;height:570px}
.hero-photo{position:absolute;inset:0;background:linear-gradient(90deg,#2b2f36 0%,#3a4450 35%,#2f4660 60%,#1f3a55 100%)}
.hero .brand{left:600px;top:150px;width:520px;font-size:62px;text-align:center;letter-spacing:2px}
.hero .btn{left:755px;top:380px;width:207px;height:52px;font-size:21px}
.scroll-hint{position:absolute;left:843px;top:498px}

/* about */
.about{top:665px;height:740px;background:var(--white)}
.about-band{position:absolute;left:918px;top:0;width:282px;height:740px;background:var(--blue-deep)}
.about-video{position:absolute;left:667px;top:105px;width:443px;height:530px;background:linear-gradient(160deg,#cfd6e2 0%,#8e98aa 40%,#3b3f48 100%)}
.play{position:absolute;left:855px;top:334px}
.section-title{position:absolute;font-family:'Cinzel',serif;font-size:36px;line-height:1.25;color:var(--ink)}
.section-title b{font-weight:700;color:var(--blue-deep)}
.about .section-title{left:88px;top:95px}
.about .section-title b{display:block;font-size:38px}
.copy{position:absolute;font-size:15px;line-height:34px;color:var(--text)}
.about .copy.first{left:90px;top:215px;width:515px}
.about .copy.second{left:90px;top:420px;width:515px}
.about .btn{left:90px;top:580px;width:220px;height:53px}

/* coaching */
.coaching{top:1405px;height:558px}
.coaching-photo{position:absolute;inset:0;background:linear-gradient(90deg,#3b3e44 0%,#2a2d33 30%,#1c1e24 60%,#23262d 100%)}
.coaching .section-title{left:502px;top:118px;color:var(--white);font-size:40px}
.coaching .copy{left:503px;top:190px;width:615px;font-size:16px;color:#e6e6e6}
.coaching .btn{left:505px;top:372px;width:215px;height:51px}

/* testimonials */
.testimonials{top:1963px;height:677px;background:var(--white)}
.testimonials h2{position:absolute;left:0;width:1200px;top:95px;text-align:center;font-family:'Cinzel',serif;font-weight:700;font-size:44px;color:var(--ink)}
.card{position:absolute;top:232px;width:325px;height:248px;background:var(--white);box-shadow:0 2px 14px rgba(0,0,0,.12);text-align:center}
.avatar{position:absolute;left:112px;top:-50px;width:100px;height:100px;border-radius:50%;background:linear-gradient(160deg,#c9b6a3,#6f5a4c)}
.card h3{position:absolute;top:77px;width:100%;font-weight:400;font-size:15px;color:var(--ink)}
.card p{position:absolute;top:115px;left:32px;width:261px;font-size:14.5px;line-height:24px;color:var(--muted)}
.dots{position:absolute;top:558px;left:572px;display:flex;gap:13px}
.dots span{width:10px;height:10px;border-radius:50%;background:#cfcfcf}
.dots span:first-child{background:var(--blue-deep)}

/* about rud */
.about-rud{top:2640px;height:622px;background:var(--night)}
.rud-band{position:absolute;left:984px;top:0;width:216px;height:310px;background:var(--blue-deep)}
.rud-photo{position:absolute;left:520px;top:80px;width:680px;height:542px;background:linear-gradient(135deg,#3f86c4 0%,#4a5d74 45%,#2b2c31 75%,#dcdcdc 100%)}
.about-rud .section-title{left:90px;top:122px;color:var(--white)}
.about-rud .copy{left:93px;top:192px;width:424px;font-size:16px;color:#e6e6e6;text-align:justify}
.about-rud .btn{left:93px;top:435px;width:218px;height:52px}

/* getaway */
.getaway{top:3262px;height:443px;background:var(--white)}
.getaway .section-title{left:0;width:1200px;top:110px;text-align:center;font-size:40px}
.getaway .copy{left:130px;width:940px;top:168px;text-align:center;font-size:17px}
.field{position:absolute;top:273px;height:56px;border:1px solid #bdbdbd;border-radius:30px;padding-left:24px;display:flex;align-items:center;font-size:17px;color:#555}
.getaway .btn{left:804px;top:273px;width:272px;height:56px;font-size:19px}

/* contact bar */
.contact-bar{top:3705px;height:108px;background:var(--blue-deep);color:var(--white)}
.contact{position:absolute;top:32px;display:flex;align-items:center;gap:12px;font-size:13px;line-height:20px}
.contact .ico{width:44px;height:44px;border-radius:50%;background:var(--ink);display:flex;align-items:center;justify-content:center}

/* footer */
.site-footer{top:3813px;height:312px;background:var(--ink);color:var(--white)}
.site-footer .brand{left:0;width:1200px;top:55px;text-align:center;font-size:30px}
.social{position:absolute;top:166px;left:503px;display:flex;gap:9px}
.social span{width:40px;height:40px;border-radius:50%;border:2px solid var(--white)}
.foot-nav{position:absolute;top:240px;width:1200px;text-align:center;font-size:13px}
.copyright{position:absolute;top:276px;width:1200px;text-align:center;font-size:13px}
</style>
</head>
<body>

<header class="site-header">
  <div class="brand">Steady Harbor<br>Roundtable</div>
  <nav class="main-nav">
    <span>Home</span><span>About Us</span><span>Coaching</span><span>Podcast</span><span>Blog</span><span>Experiences</span><span>Resources</span><span>Contact Us</span>
  </nav>
</header>

<section class="hero">
  <div class="hero-photo" role="img" aria-label="Portrait of Rud in a suit seated at a desk, city skyline at dusk behind"></div>
  <div class="brand">Steady Harbor<br>Roundtable</div>
  <a class="btn btn-solid">Get a Quote</a>
  <svg class="scroll-hint" width="30" height="62" viewBox="0 0 30 62" fill="none" stroke="#fff" stroke-width="2.5">
    <rect x="3" y="2" width="24" height="38" rx="12"/>
    <line x1="15" y1="10" x2="15" y2="20"/>
    <line x1="15" y1="44" x2="15" y2="58"/>
    <polyline points="9,52 15,58 21,52"/>
  </svg>
</section>

<section class="about">
  <div class="about-band"></div>
  <div class="about-video" role="img" aria-label="Video still of Rud speaking at a podium"></div>
  <svg class="play" width="70" height="70" viewBox="0 0 70 70">
    <circle cx="35" cy="35" r="35" fill="#0a7fd0"/>
    <polygon points="28,23 50,35 28,47" fill="#fff"/>
  </svg>
  <h2 class="section-title">ABOUT <b>STEADY HARBOR</b></h2>
  <p class="copy first">Lorem ipsum dolor sit amet, consectetur adipiscing elit, sed do eiusmod tempor incididunt ut labore et dolore magna aliqua. Ut enim ad minim veniam, quis nostrud exercitation ullamco laboris nisi ut aliquip ex ea commodo consequat. Duis aute irure dolor in reprehenderit in voluptate velit esse cillum dolore eu fugiat nulla pariatur.</p>
  <p class="copy second">Lorem ipsum dolor sit amet, consectetur adipiscing elit, sed do eiusmod tempor incididunt ut labore et dolore magna aliqua. Ut enim ad minim veniam, quis nostrud</p>
  <a class="btn btn-outline">Join Our Workshop</a>
</section>

<section class="coaching">
  <div class="coaching-photo" role="img" aria-label="Rud standing in a suit, hands in conversation in the background"></div>
  <h2 class="section-title">PERSONAL <b>COACHING</b></h2>
  <p class="copy">Sed ut perspiciatis unde omnis iste natus error sit voluptatem accusantium doloremque laudantium, totam rem aperiam, eaque ipsa quae ab illotoretatis et quasi architecto beatae vitae dicta sunt explicabo. Nemo enim ipsamtatem quia voluptas sit aspernatur aut odit aut fugit, sed quia consequuntur.</p>
  <a class="btn btn-outline on-dark">Get a Quote</a>
</section>

<section class="testimonials">
  <h2>Testimonials</h2>
  <div class="card" style="left:90px">
    <div class="avatar" role="img" aria-label="Portrait of Lena Marsh"></div>
    <h3>Lena Marsh</h3>
    <p>Sed ut perspiciatis unde omnis iste natus error sit voluptatem arem aperiam, eaque ipsa quae ab illve sa quae ab illve</p>
  </div>
  <div class="card" style="left:437px">
    <div class="avatar" role="img" aria-label="Portrait of Jonah Pell"></div>
    <h3>Jonah Pell</h3>
    <p>Sed ut perspiciatis unde omnis iste natus error sit voluptatem arem aperiam, eaque ipsa quae ab illve sa quae ab illve</p>
  </div>
  <div class="card" style="left:784px">
    <div class="avatar" role="img" aria-label="Portrait of Henry Dalt"></div>
    <h3>Henry Dalt</h3>
    <p>Sed ut perspiciatis unde omnis iste natus error sit voluptatem arem aperiam, eaque ipsa quae ab illve sa quae ab illve</p>
  </div>
  <div class="dots"><span></span><span></span><span></span></div>
</section>

<section class="about-rud">
  <div class="rud-band"></div>
  <div class="rud-photo" role="img" aria-label="Rud seated in a leather chair in front of a blue-tinted photo of smiling team members"></div>
  <h2 class="section-title">ABOUT <b>RUD</b></h2>
  <p class="copy">Sed ut perspiciatis unde omnis iste natus error sit ltatem accusantium doloremque laudantium, totam rem aperiam, eaque ipsa quae ab illotoretatis et quasi architecto beatae vitae dicta sunt explicabo. Nemo enim ipsamtatem quia voluptas sit aspernatur aut odit aut fugit, sed quia consequuntur.</p>
  <a class="btn btn-outline on-dark">Speak with Rud</a>
</section>

<section class="getaway">
  <h2 class="section-title">JOIN ME ON <b>A LEADERSHIP GETAWAY</b></h2>
  <p class="copy">Lorem ipsum dolor sit amet, consectetur adipiscing elit, sed do eiusmod tempor incididunt ut labore et dolore magna aliqua. Ut enim ad minim veniam, quis nostrud exercitation</p>
  <div class="field" style="left:123px;width:272px">User Name</div>
  <div class="field" style="left:419px;width:362px">Email</div>
  <a class="btn btn-solid">Join Now</a>
</section>

<section class="contact-bar">
  <div class="contact" style="left:90px">
    <span class="ico"><svg width="22" height="22" viewBox="0 0 22 22" fill="none" stroke="#fff" stroke-width="1.8"><circle cx="11" cy="11" r="9"/><ellipse cx="11" cy="11" rx="4" ry="9"/><line x1="2" y1="11" x2="20" y2="11"/></svg></span>
    <span>www.steadyharbor.com</span>
  </div>
  <div class="contact" style="left:534px">
    <span class="ico"><svg width="22" height="16" viewBox="0 0 22 16" fill="none" stroke="#fff" stroke-width="1.8"><rect x="1" y="1" width="20" height="14" rx="1"/><polyline points="1,1 11,9 21,1"/></svg></span>
    <span>Email:<br>hello@steadyharbor.com</span>
  </div>
  <div class="contact" style="left:933px">
    <span class="ico"><svg width="20" height="20" viewBox="0 0 24 24" fill="#fff"><path d="M6.6 10.8a15 15 0 0 0 6.6 6.6l2.2-2.2a1 1 0 0 1 1-.25 11.4 11.4 0 0 0 3.6.57 1 1 0 0 1 1 1V20a1 1 0 0 1-1 1A17 17 0 0 1 3 4a1 1 0 0 1 1-1h3.5a1 1 0 0 1 1 1c0 1.25.2 2.45.57 3.6a1 1 0 0 1-.25 1z"/></svg></span>
    <span>+1 555 0142 880</span>
  </div>
</section>

<footer class="site-footer">
  <div class="brand">Steady Harbor<br>Roundtable</div>
  <div class="social"><span></span><span></span><span></span><span></span></div>
  <div class="foot-nav">Home &nbsp;|&nbsp; About Us &nbsp;|&nbsp; Coaching &nbsp;|&nbsp; Podcast &nbsp;|&nbsp; Blog &nbsp;|&nbsp; Experiences &nbsp;|&nbsp; Resources &nbsp;|&nbsp; Contact Us</div>
  <div class="copyright">Copyrights © 2019, The Company Name. All rights reserved.</div>
</footer>

</body>
</html>
```